Study Lantern

StudyLantern.com will be a place for people looking for information, resources, and advisement to start or continue their education. We want a friendly, inviting site design that makes finding what potential students are looking for simple and easy to navigate. We are not committed to the colors of the logo, so variations on the color scheme are welcome.

Text instructions based on the wireframe: For the site's homepage we'd like a banner at the very top for our Logo and white space to the right of it. See attachments for logo + wireframe. Below that would be navigation. Below that split into 2/3 on the left we would have home page content, and 1/3 on the right we would have the lead form. At the bottom of the page we would have a space for types of degrees, then a footer with copyright info + site info.

See wireframes for additional page layouts.

Industry/Entity Type

Education

Requirements
Must have
• At minimum we are looking for three pages: homepage, choose your degree path page, and content page.
Nice to have
• -White space is appreciated
-Variations on the color scheme are welcome, we are not married to the existing logo's color scheme.

```html
<!DOCTYPE html>
<html lang="en">
<head>
<meta charset="utf-8">
<title>Study Lantern – Home</title>
<link href="https://fonts.googleapis.com/css2?family=Source+Sans+3:wght@400;600;700&family=PT+Sans+Narrow:wght@700&display=swap" rel="stylesheet">
<style>
:root{
  --teal:#1f4656;
  --teal-dark:#132f3b;
  --orange:#f26b21;
  --orange-dark:#e0561a;
  --text:#555;
  --text-light:#777;
  --field-border:#c9c9c9;
  --panel:#d8d8d8;
  --footer:#2e2e2e;
  --footer-edge:#050505;
  --footer-text:#bdbdbd;
}
*{box-sizing:border-box;margin:0;padding:0}
html,body{width:969px;height:1200px;overflow:hidden}
body{position:relative;background:#fff;font-family:"Source Sans 3",Arial,sans-serif;color:var(--text)}
.top-wash{position:absolute;left:0;top:0;width:969px;height:446px;background:linear-gradient(#fff 0%,#f1f1f1 60%,#e2e2e2 100%)}
.abs{position:absolute}

.brand{left:52px;top:60px;display:flex;align-items:center;gap:12px}
.brand-mark{width:22px;height:22px;background:var(--orange)}
.brand-name{font-size:46px;font-weight:700;color:var(--teal);letter-spacing:-1px;line-height:1}

.call{left:740px;top:70px;font-size:16px;line-height:24px}
.call-label{color:var(--orange);position:absolute;left:0;top:0;white-space:nowrap}
.call-nums{position:absolute;left:81px;top:0;color:#333;white-space:nowrap}

.nav{left:46px;top:139px;width:874px;height:40px;background:linear-gradient(#2d5a6c,var(--teal-dark));}
.nav a{position:absolute;top:0;height:40px;line-height:40px;color:#fff;font-size:13px;text-decoration:none}
.nav .active{left:0;width:96px;background:var(--orange);text-align:center;top:0;height:40px;line-height:40px}
.search{position:absolute;left:740px;top:9px;width:114px;height:22px;border-radius:11px;background:#fff;border:1px solid #9ab;font-size:12px;font-style:italic;color:#444;padding-left:16px;line-height:20px}
.search svg{position:absolute;right:8px;top:5px}

.hero{left:48px;top:194px;width:867px;height:324px;background:linear-gradient(100deg,#e6e0da 0%,#c9c3bd 35%,#efeeee 55%,#b9a8a0 80%,#e5e8ec 100%)}
.hero-shadow{left:0;top:446px;width:969px;height:90px;background:radial-gradient(ellipse 55% 60% at 50% 0%,rgba(0,0,0,.18),rgba(0,0,0,0) 70%)}
.arrow{top:341px;width:44px;height:46px;background:rgba(140,140,140,.85);color:#fff;font-size:28px;line-height:44px;text-align:center}

.welcome{left:47px;top:545px;font-size:16px;color:var(--teal)}
.welcome span{color:var(--orange)}
.copy{left:47px;width:554px;font-size:10.5px;line-height:22.3px;text-align:justify;color:var(--text-light)}

.types{left:46px;top:846px;width:552px;height:163px;border:1px solid #aaa;padding:5px}
.types-inner{height:100%;background:linear-gradient(#ececec,#fff 45%);position:relative}
.types h2{position:absolute;left:14px;top:14px;font-weight:400;font-size:16px;color:var(--orange)}
.types ul{position:absolute;list-style:none;font-size:10.5px;color:#333;line-height:14px}
.types li{position:relative;padding-left:17px;margin-bottom:10px}
.types li::before{content:"";position:absolute;left:2px;top:4px;width:7px;height:7px;border-radius:50%;background:#444}

.lead-title{left:631px;top:552px;font-size:16px;font-weight:700;color:var(--orange)}
.lead-sub{left:631px;top:582px;width:270px;font-size:10.5px;line-height:17px;color:var(--text-light)}
.lead{left:628px;top:624px;width:292px;height:387px;background:#fbfbfb;box-shadow:0 0 4px rgba(0,0,0,.15)}
.lead-panel{position:absolute;left:4px;top:3px;width:284px;height:379px;background:linear-gradient(#f2f2f2,var(--panel))}
.lead-head{position:absolute;left:0;top:0;width:284px;height:41px;background:linear-gradient(var(--orange),var(--orange-dark));color:#fff;font-family:"PT Sans Narrow",Arial,sans-serif;font-weight:700;font-size:16px;line-height:44px;padding-left:12px}
.row{position:absolute;left:15px;font-size:10.5px;line-height:14px;color:#333}
.field{position:absolute;height:24px;background:#fff;border:1px solid var(--field-border)}
.field.select::after{content:"";position:absolute;right:8px;top:9px;border:4px solid transparent;border-top:5px solid #333}
.submit{left:700px;top:990px;width:158px;height:38px;background:linear-gradient(#2d5a6c,var(--teal-dark));border-radius:3px;color:#fff;font-size:12.5px;font-weight:600;text-align:center;line-height:38px;letter-spacing:.2px}

.footer{left:0;top:1057px;width:969px;height:143px;background:var(--footer-edge)}
.footer-inner{position:absolute;left:46px;top:0;width:876px;height:143px;background:var(--footer)}
.footer-links{position:absolute;left:11px;top:25px;font-size:12.5px;color:var(--footer-text);white-space:pre}
.footer-copy{position:absolute;left:11px;top:47px;font-size:12.5px;color:var(--footer-text)}
.footer-contact{position:absolute;left:663px;top:23px;font-size:16px;font-weight:600;color:#e5e5e5}
.footer-label{position:absolute;left:661px;top:55px;font-size:12.5px;color:var(--orange)}
.footer-address{position:absolute;left:727px;top:55px;font-size:12.5px;line-height:22px;color:var(--footer-text)}
</style>
</head>
<body>
<div class="top-wash"></div>

<header>
  <div class="abs brand"><span class="brand-mark"></span><span class="brand-name">Study Lantern</span></div>
  <div class="abs call"><span class="call-label">CALL US :</span><span class="call-nums">555-014-2200<br>555-014-2201</span></div>
</header>

<nav class="abs nav">
  <a class="active" href="#">Home</a>
  <a href="#" style="left:125px">About Us</a>
  <a href="#" style="left:213px">Privacy Policy</a>
  <a href="#" style="left:330px">Terms of Use</a>
  <a href="#" style="left:469px">Feedback</a>
  <a href="#" style="left:550px">Contact Us</a>
  <div class="search">Search
    <svg width="11" height="11" viewBox="0 0 11 11"><circle cx="4.5" cy="4.5" r="3.3" fill="none" stroke="#777" stroke-width="1.2"/><line x1="7" y1="7" x2="10" y2="10" stroke="#777" stroke-width="1.4"/></svg>
  </div>
</nav>

<div class="abs hero-shadow"></div>
<div class="abs hero" role="img" aria-label="Photo of a group of students studying together at a table"></div>
<div class="abs arrow" style="left:48px">&laquo;</div>
<div class="abs arrow" style="left:871px">&raquo;</div>

<main>
  <h1 class="abs welcome" style="font-weight:400">Welcome to Study <span>Lantern</span></h1>
  <p class="abs copy" style="top:585px">StudyLantern.com is a free resource to start your path to a college degree and compare higher education options that can generally lead to improved career or job opportunities based on numerous employment reports from organizations like the National Workforce Survey Office. Our free education tools and resources do not guarantee employment nor an offer of employment.</p>
  <p class="abs copy" style="top:710px">Our mission is to match you with the top colleges, universities or technical institutions that offer the higher education programs that meet your goals, based on the information you provided. Enrollment and Education Experts at the Private &amp; Public Institutions we partner with can provide you with additional, detailed information on a) applying for their school b) tuition costs and tuition assistance for their school and c) career and employment information and statistics for students that have successfully completed programs in that field or from their particular school.</p>

  <section class="abs types">
    <div class="types-inner">
      <h2>Degree Types</h2>
      <ul style="left:22px;top:50px;width:290px">
        <li>Lorem ipsum dolor sit amet, consectetur adipiscing elit.</li>
        <li>Fusce nec velit eget massa tristique lacinia vel eget est.</li>
        <li>Mauris sit amet est libero, quis vestibulum tellus.</li>
      </ul>
      <ul style="left:308px;top:50px;width:230px">
        <li>Lorem ipsum dolor sit amet, consectetur adipiscing elit.</li>
        <li>Fusce nec velit eget massa tristique lacinia vel eget est.</li>
      </ul>
    </div>
  </section>
</main>

<aside>
  <h2 class="abs lead-title">Tell us more about YOU!</h2>
  <p class="abs lead-sub">StudyLantern provides you with accredited school information that match your interests.</p>
  <form class="abs lead">
    <div class="lead-panel">
      <div class="lead-head">Get matched to the right schools today.</div>
      <div class="row" style="top:66px">Subject*</div>
      <div class="field select" style="left:128px;top:59px;width:143px"></div>
      <div class="row" style="top:93px">Choose OneDegree<br>Level*</div>
      <div class="field select" style="left:128px;top:92px;width:143px"></div>
      <div class="row" style="top:128px">Choose OneHigh<br>&nbsp;School Grad Yr.*</div>
      <div class="field select" style="left:128px;top:127px;width:143px"></div>
      <div class="row" style="top:165px">Choose OneFirst Name*</div>
      <div class="field" style="left:128px;top:161px;width:143px"></div>
      <div class="row" style="top:199px">Last Name*</div>
      <div class="field" style="left:128px;top:195px;width:143px"></div>
      <div class="row" style="top:232px">Street Address*</div>
      <div class="field" style="left:128px;top:230px;width:143px"></div>
      <div class="row" style="top:267px">Zip / City / State*</div>
      <div class="field" style="left:128px;top:261px;width:37px"></div>
      <div class="field" style="left:169px;top:261px;width:60px"></div>
      <div class="field" style="left:233px;top:261px;width:38px"></div>
      <div class="row" style="top:302px">Phone Number*</div>
      <div class="field" style="left:128px;top:294px;width:143px"></div>
      <div class="row" style="top:336px">Email Address*</div>
      <div class="field" style="left:128px;top:328px;width:143px"></div>
    </div>
  </form>
  <div class="abs submit">REQUEST INFORMATION</div>
</aside>

<footer class="abs footer">
  <div class="footer-inner">
    <div class="footer-links">Home  |    About Us  |   Privacy Policy  |  Terms of Use   |    Feedback  |  Contact Us</div>
    <div class="footer-copy">Co[yright@ 2012. All Rights Reerved</div>
    <div class="footer-contact">Contact Us</div>
    <div class="footer-label">Address:</div>
    <div class="footer-address">&nbsp;StudyLantern.com<br>42 Orchard Lane<br>Fairhaven, CA 90000</div>
  </div>
</footer>
</body>
</html>
```